Plastic Business Card for Bookkeeper

We are looking for a simple professional business card design to use for printing on thin frosted plastic (see-through) card stock. Logo and brand guideline documents are attached as well as a photo of our old business card, and another business card example that we like.

Target Market(s)

Small Business

Industry/Entity Type

Bookkeeper

Contact Information for Business Card

Harriet Valdez CPA
Chief Executive Bookkeeper
T. 03 5926 4187
M. 0432 861 507
E. harriet@quillpathledger.com
W. www.quillpathledger.com

Font styles to use
Sans Serif

Colors
6b449b
00a990

Requirements
Must have
• Stick with logo colors. Writing should be clear and easy to read and not too cramped together.
Nice to have
• Tag line for back of the card - 'Not your ordinary Bookkeeper'

```html
<!DOCTYPE html>
<html lang="en">
<head>
<meta charset="utf-8">
<title>Quillpath Ledger – Business Card</title>
<link rel="stylesheet" href="https://fonts.googleapis.com/css2?family=Open+Sans:wght@400;600&display=swap">
<style>
  :root {
    --page: #e6e4e1;
    --card: #f4f3f0;
    --purple: #6b449b;
    --teal: #1e7e7b;
    --ink: #333333;
    --on-teal: #ddd5cc;
    --on-purple: #f1ecf6;
  }
  * { margin: 0; padding: 0; box-sizing: border-box; }
  html, body {
    width: 1200px;
    height: 1047px;
    overflow: hidden;
    background: var(--page);
    font-family: "Open Sans", Arial, sans-serif;
  }
  .business-card {
    position: absolute;
    left: 80px;
    top: 242px;
    width: 1040px;
    height: 563px;
    border-radius: 22px;
    background: var(--card);
    overflow: hidden;
    box-shadow: 0 2px 10px rgba(0,0,0,0.08);
  }
  .card-shapes {
    position: absolute;
    inset: 0;
    width: 100%;
    height: 100%;
  }
  .brand-name {
    position: absolute;
    left: 118px;
    top: 150px;
    color: var(--purple);
    font-weight: 600;
    font-size: 29px;
    line-height: 40px;
    letter-spacing: 0.5px;
  }
  .holder {
    position: absolute;
    right: 42px;
    top: 178px;
    text-align: right;
    color: var(--on-purple);
  }
  .holder-name {
    font-weight: 600;
    font-size: 40px;
    line-height: 48px;
  }
  .holder-title {
    font-weight: 400;
    font-size: 23px;
    line-height: 30px;
    margin-right: -6px;
  }
  .address {
    position: absolute;
    left: 74px;
    top: 312px;
    color: var(--ink);
    font-size: 24px;
    line-height: 32px;
  }
  .contact {
    position: absolute;
    display: flex;
    align-items: center;
    gap: 12px;
    color: var(--on-teal);
    font-size: 26px;
    line-height: 34px;
  }
  .contact svg { width: 24px; height: 24px; fill: var(--on-teal); flex: none; }
  .contact--phone { left: 70px; top: 440px; }
  .contact--mobile { left: 70px; top: 488px; }
  .contact--email { left: 392px; top: 440px; }
  .contact--web { left: 392px; top: 488px; }
</style>
</head>
<body>
  <div class="business-card">
    <svg class="card-shapes" viewBox="0 0 878 475" preserveAspectRatio="none" aria-hidden="true">
      <path d="M0,318 L560,318 C640,318 655,292 685,248 C718,198 742,132 800,118 L878,112 L878,475 L0,475 Z" fill="var(--teal)"/>
      <path d="M0,316 L560,316 C638,316 652,290 682,246 C715,196 740,128 800,114 L878,108" fill="none" stroke="var(--purple)" stroke-width="5"/>
      <path d="M565,155 L878,155 L878,237 L565,237 Q553,237 553,225 L553,167 Q553,155 565,155 Z" fill="var(--purple)"/>
    </svg>

    <div class="brand-name">QUILLPATH<br>LEDGER</div>

    <div class="holder">
      <div class="holder-name">Valdez CPA</div>
      <div class="holder-title">Chief Executive Bookkeeper</div>
    </div>

    <div class="address">418 W. Marlow Avenue NE Arlington, VA 22201</div>

    <div class="contact contact--phone">
      <svg viewBox="0 0 24 24"><path d="M6.6 10.8a15.1 15.1 0 0 0 6.6 6.6l2.2-2.2a1 1 0 0 1 1-.25 11.4 11.4 0 0 0 3.6.57 1 1 0 0 1 1 1V20a1 1 0 0 1-1 1A17 17 0 0 1 3 4a1 1 0 0 1 1-1h3.5a1 1 0 0 1 1 1c0 1.25.2 2.45.57 3.57a1 1 0 0 1-.25 1z"/></svg>
      <span>03 5926 4187</span>
    </div>
    <div class="contact contact--mobile">
      <svg viewBox="0 0 24 24"><path d="M8 2h8a2 2 0 0 1 2 2v16a2 2 0 0 1-2 2H8a2 2 0 0 1-2-2V4a2 2 0 0 1 2-2zm0 3v13h8V5zm4 14.2a.9.9 0 1 0 0 1.8.9.9 0 0 0 0-1.8z"/></svg>
      <span>0432 861 507</span>
    </div>
    <div class="contact contact--email">
      <svg viewBox="0 0 24 24"><path d="M3 5h18a1 1 0 0 1 1 1v12a1 1 0 0 1-1 1H3a1 1 0 0 1-1-1V6a1 1 0 0 1 1-1zm1 3v9h16V8l-8 5z"/></svg>
      <span>harriet@quillpathledger.com</span>
    </div>
    <div class="contact contact--web">
      <svg viewBox="0 0 24 24"><path d="M12 2a10 10 0 1 0 0 20 10 10 0 0 0 0-20zm-1 17.9A8 8 0 0 1 4.1 10L9 15v1a2 2 0 0 0 2 2zm6.9-2.5A2 2 0 0 0 16 16h-1v-3a1 1 0 0 0-1-1H8v-2h2a1 1 0 0 0 1-1V7h2a2 2 0 0 0 2-2v-.4a8 8 0 0 1 2.9 12.8z"/></svg>
      <span>www.quillpathledger.com</span>
    </div>
  </div>
</body>
</html>
```